Online-Marketing Material für Nachhilfeschule
Quintessa hat superschnell gearbeitet, vorher selbst recherchiert, um sofort das zu meiner Webseite passende Produkt zu erstellen. Da es eine Kooperation in diesem Fall gab, hat er beide Webseiten für seine Produktvorschläge als Wunschvorstellung ausgesucht und angewendet. Perfekt! That's quintessa! Thank you!
Zielgruppe
Ich habe am 1.7. eine Nachhilfeschule gegründet. Nun möchte ich ein Pilotprojekt starten, um Schülern in der Abiturklasse - Gymnasium oder Berufsschule - , die exzellente Zensuren wollen, zu herausragenden Noten zu verhelfen.
Dieser Banner wird durch den Lehrer den Schülern per Email oder WhatsApp überreicht.
Ich stelle mir ein junges und dynamisches Design vor. Das schwarz/grüne Logo der Fahrschule gefällt mir besser (wenn das andere Eurer Meinung nach besser passt, geht auch das). Das Schwarz-weiß-Logo vom Wissensnest muss aber dominanter sein!
Mein Kooperationspartner, eine Fahrschule, stellt ihre Räume zur Verfügung. Meine Gegenleistung: Nennung in der Werbung.
Aufgabenstellung
Zielgruppe: Abiturienten,
- die Gas geben wollen, damit sie bessere Chancen am Arbeitsmarkt haben.
- die bereit sind, 4 Samstage herzugeben, um noch mehr zu lernen ...
- die selbst, oder deren Eltern, bereit sind, für diese Chancen Geld auszugeben
- die bei der Anmeldung aufgezeigt bekommen, dass das Bonbon eine Vermittlung zu ihrem Wunschunternehmen und ihrer Wunschposition ist.
Das Bonbon bitte Fahrschul-Logo-grün machen, vielleicht auch mit Punkten - vom Wissensnest-Logo ...
Die Texte sind in der Word-Datei. Wichtig: Sie müssen bearbeitet werden können, da sich die Daten wie z.B. Datum, Preis, Fächer, etc. ändern können. Wenn die Kurse angenommen werden, wird der Gewinner zukünftig meine gesamte Werbung gestalten -> CI

```html
<!DOCTYPE html>
<html lang="de">
<head>
<meta charset="utf-8">
<title>Wissensnest – Ich geb Gas fürs Abi</title>
<link href="https://fonts.googleapis.com/css2?family=Poppins:ital,wght@0,400;0,500;0,600;0,700;0,800;1,500;1,800&family=Raleway:wght@400;800&display=swap" rel="stylesheet">
<style>
  :root {
    --blue: #1b4a9c;
    --magenta: #c4167f;
    --cream: #f7f1ef;
    --white: #ffffff;
    --ink: #111111;
    --green: #4ee01e;
  }
  * { margin: 0; padding: 0; box-sizing: border-box; }
  html, body { width: 848px; height: 1200px; overflow: hidden; background: var(--white); }
  .poster {
    position: relative; width: 848px; height: 1200px; overflow: hidden;
    font-family: "Poppins", sans-serif; background: var(--cream);
  }
  .hero-photo {
    position: absolute; left: 0; top: 0; width: 848px; height: 590px;
    background: linear-gradient(180deg, #f4f6f2 0%, #eef0ea 22%, #c9b3a6 34%, #6f7fb0 52%, #5a5aa8 68%, #8a3d96 80%, #c4167f 88%, #c4167f 100%);
  }
  .headline {
    position: absolute; left: 54px; top: 44px;
    font-weight: 800; font-style: italic; font-size: 52px; line-height: 62px;
    color: var(--blue); letter-spacing: -1px; white-space: nowrap;
  }
  .headline .accent { color: var(--magenta); }
  .brand-panel {
    position: absolute; left: 432px; top: 30px; width: 386px; height: 142px;
    background: var(--white);
  }
  .brand {
    position: absolute; left: 24px; top: 34px; display: flex; align-items: center; gap: 16px;
  }
  .brand-dot { width: 44px; height: 44px; border-radius: 50%; background: var(--blue); }
  .brand-name { font-weight: 500; font-size: 46px; color: var(--blue); letter-spacing: -0.5px; }
  .brand-tagline {
    position: absolute; left: 146px; top: 106px; font-size: 16px; font-weight: 500; color: var(--blue);
  }
  .magenta-band {
    position: absolute; left: 0; top: 490px; width: 848px; height: 100px;
    font-family: "Raleway", sans-serif; color: var(--white); white-space: nowrap;
  }
  .band-lead { position: absolute; left: 43px; top: 4px; font-size: 32px; font-weight: 400; }
  .band-gene { position: absolute; left: 43px; top: 48px; font-size: 30.5px; font-weight: 800; }
  .blue-band {
    position: absolute; left: 0; top: 590px; width: 848px; height: 62px; background: var(--blue);
  }
  .blue-band p {
    position: absolute; left: 40px; top: 9px; font-size: 29px; font-weight: 600; color: var(--white); white-space: nowrap;
  }
  .fact { position: absolute; }
  .fact-tag {
    display: inline-block; background: var(--magenta); color: var(--white);
    font-size: 24px; font-weight: 600; padding: 4px 16px 6px; transform: rotate(-1.5deg); white-space: nowrap;
  }
  .fact-value {
    margin-top: 12px; margin-left: 16px;
    font-size: 19.5px; font-weight: 700; line-height: 24px; color: var(--blue); white-space: nowrap;
  }
  .extra-title {
    position: absolute; left: 234px; top: 928px; font-size: 31px; font-weight: 600; color: var(--magenta);
  }
  .extra-line { position: absolute; top: 972px; font-size: 22.5px; font-weight: 500; color: var(--ink); white-space: nowrap; }
  .extra-line.left { left: 182px; }
  .extra-line.right { left: 475px; }
  .candy {
    position: absolute; left: 378px; top: 945px; width: 86px; height: 78px; border-radius: 50%;
    background: radial-gradient(circle at 35% 35%, #b9ff8c 0%, #5de826 45%, #2fb50f 100%);
    transform: rotate(-30deg);
  }
  .contact { position: absolute; left: 56px; top: 1054px; color: var(--blue); white-space: nowrap; }
  .contact-lead { font-size: 20px; font-weight: 500; }
  .contact-phone { font-size: 34px; font-weight: 800; line-height: 44px; }
  .partner-label {
    position: absolute; right: 49px; top: 1030px; font-size: 19px; font-style: italic; font-weight: 500; color: var(--ink);
  }
  .partner {
    position: absolute; left: 548px; top: 1060px; width: 254px; height: 60px;
    border-left: 3px solid var(--green);
  }
  .partner-name {
    position: absolute; left: 14px; top: 2px; display: flex; align-items: center; gap: 8px;
    font-size: 19px; line-height: 26px; font-weight: 800; color: #2a2a2a; white-space: nowrap;
  }
  .partner-square { width: 14px; height: 14px; background: var(--green); flex: none; }
  .partner-tagline {
    position: absolute; left: 18px; top: 34px; font-size: 15.5px; line-height: 20px; font-style: italic; font-weight: 500; color: #333; white-space: nowrap;
  }
  .footer {
    position: absolute; left: 0; top: 1143px; width: 848px; height: 57px; background: var(--blue);
    display: flex; align-items: center; justify-content: center;
  }
  .footer p { font-size: 19px; font-weight: 700; color: var(--white); }
</style>
</head>
<body>
<main class="poster">
  <div class="hero-photo" role="img" aria-label="Foto: fünf lachende junge Abiturienten sitzen Arm in Arm im Freien"></div>

  <h1 class="headline">„ICH <span class="accent">GEB GAS</span><br>FÜRS ABI!“</h1>

  <div class="brand-panel">
    <div class="brand">
      <span class="brand-dot"></span>
      <span class="brand-name">Wissensnest</span>
    </div>
    <p class="brand-tagline">Nachhilfe seit 1974</p>
  </div>

  <section class="magenta-band">
    <p class="band-lead">Du stehst kurz vorm Abi und hast in dir das</p>
    <p class="band-gene">ICH WILL BERUFLICH ERFOLGREICH SEIN-GEN?</p>
  </section>

  <section class="blue-band">
    <p>Dann gib Gas und du bist in der Pole-Position!</p>
  </section>

  <div class="fact" style="left:53px; top:678px;">
    <span class="fact-tag">Start wann?</span>
    <p class="fact-value">Ab 21. Januar 2023</p>
  </div>
  <div class="fact" style="left:272px; top:680px;">
    <span class="fact-tag">Womit?</span>
    <p class="fact-value">Mathe oder Englisch<br>oder Spanisch</p>
  </div>
  <div class="fact" style="left:541px; top:680px;">
    <span class="fact-tag">Wie oft?</span>
    <p class="fact-value">An 4 Samstagen,<br>je 2 x 90 Minuten</p>
  </div>
  <div class="fact" style="left:51px; top:797px;">
    <span class="fact-tag">Wie viele?</span>
    <p class="fact-value">2 bis 6 Schüler</p>
  </div>
  <div class="fact" style="left:283px; top:797px;">
    <span class="fact-tag">Welcher Preis?</span>
    <p class="fact-value">Ab 295 Euro, inklusive<br>Lernmaterialien</p>
  </div>
  <div class="fact" style="left:541px; top:797px;">
    <span class="fact-tag">Location?</span>
    <p class="fact-value">KRV Fahrschule,<br>Lindenweg 8,<br>78462 Seehafen</p>
  </div>

  <p class="extra-title">Zugabe:</p>
  <p class="extra-line left">Unbezahlbares</p>
  <div class="candy" role="img" aria-label="Illustration: grünes Bonbon"></div>
  <p class="extra-line right">für Durchstarter!</p>

  <div class="contact">
    <p class="contact-lead">Mehr Infos zur Anmeldung unter</p>
    <p class="contact-phone">+49 170 555 21 908</p>
  </div>

  <p class="partner-label">Unser Partner:</p>
  <div class="partner">
    <div class="partner-name"><span class="partner-square"></span>KRV-Team Fahrschule</div>
    <p class="partner-tagline">Ausbildung &amp; Weiterbildung</p>
  </div>

  <footer class="footer">
    <p>www.wissensnest.de/seeland</p>
  </footer>
</main>
</body>
</html>
```